Hardcore nerd needs to stand out in a sea of dull Defence business cards

Wombat Devices is a new Australian consulting engineering company that turns research and theory into practical systems. No evangelistic fluff, just mathematics and physics into electronic and optical circuits for consumer products, scientific research or Defence applications.

We already have a recognised logo (provided) which is often dark blue/black on a light background but we're open to other combinations. (Us engineers tend to have limited aesthetic imagination :)

Some of our recent products have included:
* Instrumentation for electrical testing,
* Radar jammers,
* GPS antenna design,
* Satellite tracking systems,
* High power lasers

We're open to both single and double-sided designs - happy to be convinced either way.

P.S. Another group is working on the web page, so - alas - our web site is currently of no use for images/ideas...

Target Market(s)

Engineering managers,
Scientists

Contact Information for Business Card

Dr Colin Marsh
R&D Engineer

colin@wombatdevicesco.com.au
0427 563 210

PO Box XXX (to be confirmed)
Banks ACT 2913
Australia

Font styles to use
Serif
Sans Serif

Colors

Designer to choose colors to be used in the design.

Requirements
Must have
• My contact details!
• I've had many (great) "bold and plain" designs submitted already, so feel free to be artistically creative :)
• Happy to take advice re fonts/colours/printability etc.
Nice to have
• I'm not sure if "lists" are more at home on a CV than a business card, but representative services include:
• Applied electromagnetics
• RF and high speed electronics
• Signal and image processing
• Electro-optical and laser systems
• Concept-to-prototype design services
• If you're considering double sided cards, then often measuring/alignment grids/rulers feature on the back of similar cards.
• e.g. https://www.lumoptix-example.com/newgrouppage9.cfm?objectgroup_id=4815
• https://www.lumoptix-example.com/newgrouppage9.cfm?objectgroup_ID=4817
• ..or even a "Smith chart" (google will return lots)
• Generic images to represent a capability might work - googling images associated with keyword for each of these areas might help:
• - "passive radar", "phased array", "fdtd", "vircator"
• RF and high speed electronic design
• - "smith chart", "microstrip circuits", "dimensioned drawing", "electronic schematic"
• - "dft", "iir filter"
• - "optical cavity". "laser energy level diagram"
• Background/watermarked images outlines/wireframes/schematics would probably look OK.
Should not have
• If a list of projects/services is provided, it is important not to make the client feel that this is "all" the company can do. Engineering design is a creative discipline (like graphics :)
• Please, no stock "military" snaps like planes, missiles, etc!

```html
<!DOCTYPE html>
<html lang="en">
<head>
<meta charset="utf-8">
<title>Wombat Devices – Business Card</title>
<link href="https://fonts.googleapis.com/css2?family=Lato:wght@400;700;900&display=swap" rel="stylesheet">
<style>
  :root {
    --backdrop: #2b2b2b;
    --card: #050505;
    --accent-blue: #2c3b80;
    --text-white: #ffffff;
    --text-grey: #7a7a7a;
    --watermark: #1c1c1c;
  }
  * { box-sizing: border-box; margin: 0; padding: 0; }
  html, body {
    width: 1200px; height: 970px; overflow: hidden;
    background: var(--backdrop);
    font-family: "Lato", sans-serif;
  }
  .canvas {
    position: relative; width: 1200px; height: 970px;
    display: flex; flex-direction: column; align-items: center; justify-content: center; gap: 40px;
  }
  .card {
    position: relative; width: 760px; height: 434px;
    background: var(--card); overflow: hidden;
    box-shadow: 0 10px 30px rgba(0,0,0,.5);
  }
  .card::after {
    content: ""; position: absolute; left: 0; right: 0; bottom: 0; height: 6px;
    background: var(--accent-blue);
  }

  /* Front */
  .brand { position: absolute; left: 56px; top: 62px; display: flex; align-items: center; gap: 16px; }
  .brand-dot { width: 54px; height: 54px; border-radius: 50%; background: var(--text-white); }
  .brand-name { color: var(--text-white); font-weight: 900; font-size: 34px; letter-spacing: 1px; text-transform: uppercase; }

  .person { position: absolute; right: 48px; top: 128px; text-align: right; }
  .person-name { color: var(--text-white); font-weight: 900; font-size: 40px; }
  .person-role { color: var(--text-grey); font-size: 20px; margin-top: 2px; }
  .accent-square { position: absolute; right: 0; top: 92px; width: 22px; height: 70px; background: var(--accent-blue); }

  .address { position: absolute; left: 56px; top: 250px; color: var(--text-grey); font-size: 20px; line-height: 1.3; }
  .contacts { position: absolute; left: 56px; top: 312px; list-style: none; }
  .contacts li { display: flex; align-items: center; gap: 14px; color: var(--text-grey); font-size: 19px; line-height: 1.6; }
  .contacts svg { width: 18px; height: 18px; flex: none; }

  /* Back */
  .watermark {
    position: absolute; right: -40px; top: 20px; width: 420px; height: 420px;
    border-radius: 50%; background: var(--watermark);
  }
  .products { position: absolute; left: 70px; top: 90px; color: var(--text-white); }
  .products-title { font-weight: 900; font-size: 40px; letter-spacing: 1px; margin-bottom: 14px; }
  .products-list { list-style: none; padding-left: 36px; }
  .products-list li { position: relative; font-size: 25px; line-height: 1.55; }
  .products-list li::before {
    content: ""; position: absolute; left: -34px; top: 50%; transform: translateY(-50%);
    width: 16px; height: 16px; border-radius: 50%; background: var(--text-white);
  }
</style>
</head>
<body>
<main class="canvas">
  <section class="card card-front" aria-label="Card front">
    <div class="brand">
      <span class="brand-dot"></span>
      <span class="brand-name">Wombat Devices</span>
    </div>

    <div class="person">
      <p class="person-name">Dr Colin Marsh</p>
      <p class="person-role">R&amp;D Engineer</p>
    </div>
    <span class="accent-square"></span>

    <p class="address">PO Box XXX<br>Banks ACT 2913, Australia</p>

    <ul class="contacts">
      <li>
        <svg viewBox="0 0 24 24" fill="#fff"><path d="M6.6 10.8a15.1 15.1 0 0 0 6.6 6.6l2.2-2.2a1 1 0 0 1 1-.25 11.4 11.4 0 0 0 3.6.57 1 1 0 0 1 1 1V20a1 1 0 0 1-1 1A17 17 0 0 1 3 4a1 1 0 0 1 1-1h3.5a1 1 0 0 1 1 1c0 1.25.2 2.45.57 3.57a1 1 0 0 1-.25 1z"/></svg>
        0427 563 210
      </li>
      <li>
        <svg viewBox="0 0 24 24" fill="none" stroke="#fff" stroke-width="2"><rect x="2" y="5" width="20" height="14"/><path d="M2 5l10 8 10-8"/></svg>
        colin@wombatdevicesco.com.au
      </li>
      <li>
        <svg viewBox="0 0 24 24" fill="none" stroke="#fff" stroke-width="1.8"><circle cx="12" cy="12" r="10"/><path d="M2 12h20M12 2c3 3 3 17 0 20M12 2c-3 3-3 17 0 20"/></svg>
        www.wombatdevicesco.com.au
      </li>
    </ul>
  </section>

  <section class="card card-back" aria-label="Card back">
    <span class="watermark"></span>
    <div class="products">
      <h2 class="products-title">PRODUCTS:</h2>
      <ul class="products-list">
        <li>Instrumentation for electrical testing</li>
        <li>Radar jammers</li>
        <li>GPS antenna design</li>
        <li>Satellite tracking systems</li>
        <li>High power lasers</li>
      </ul>
    </div>
  </section>
</main>
</body>
</html>
```